Business card

We are looking for a creative person to deigns our company business card.

Target Market(s)

College age student

Industry/Entity Type

Accommodation

Contact Information for Business Card

We want a fun, clean and sophisticated design. It should look good, but more importantly the information should be legible.

Font styles to use
Serif
Sans Serif
Other font styles liked:
• Open Sans ,

Colors
33a6d7

Requirements
Must have
• Must have a young and memorable message. Be legible.
• Our logo on the back on a solid blue , please find color and logo attached
• LodgeBridgely.net on the back.
Nice to have
• I would like to have couple of different fonts on the LodgeBridgely.net on the back of the cards with a solid blue.

```html
<!DOCTYPE html>
<html lang="en">
<head>
<meta charset="utf-8">
<title>LodgeBridgely Business Card</title>
<link href="https://fonts.googleapis.com/css2?family=Nunito+Sans:wght@400;600;800&family=Open+Sans:wght@400;600&display=swap" rel="stylesheet">
<style>
  :root {
    --backdrop: #2f3d45;
    --brand-blue: #33a6d7;
    --deep-blue: #0f5283;
    --navy: #0c4a78;
    --card-blue: #1a6aa3;
    --ink: #1b1b1b;
    --paper: #ffffff;
  }
  html, body {
    margin: 0;
    width: 1200px;
    height: 900px;
    overflow: hidden;
    background: var(--backdrop);
  }
  .canvas {
    position: relative;
    width: 1200px;
    height: 900px;
  }
  .card {
    position: absolute;
    left: 250px;
    width: 700px;
    height: 400px;
    overflow: hidden;
    box-shadow: 0 14px 30px rgba(0,0,0,0.35);
  }
  /* Back of card */
  .card-back {
    top: 30px;
    background: radial-gradient(circle at 50% 40%, #3a9ad6 0%, var(--card-blue) 45%, var(--deep-blue) 100%);
    color: var(--paper);
    text-align: center;
  }
  .back-brand {
    position: absolute;
    top: 130px;
    left: 0;
    right: 0;
    font-family: "Nunito Sans", sans-serif;
    font-weight: 800;
    font-size: 64px;
    letter-spacing: -1px;
  }
  .back-url {
    position: absolute;
    top: 268px;
    left: 0;
    right: 0;
    font-family: "Open Sans", sans-serif;
    font-size: 15px;
    letter-spacing: 6px;
  }
  /* Front of card */
  .card-front {
    top: 470px;
    background: radial-gradient(circle at 50% 10%, #ffffff 0%, #f3f3f3 70%, #ececec 100%);
  }
  .front-brand {
    position: absolute;
    left: 40px;
    top: 175px;
    width: 300px;
    text-align: center;
    font-family: "Nunito Sans", sans-serif;
    font-weight: 800;
    font-size: 40px;
    color: var(--navy);
    letter-spacing: -0.5px;
  }
  .divider {
    position: absolute;
    left: 365px;
    top: 110px;
    width: 2px;
    height: 160px;
    background: linear-gradient(to bottom, transparent, #222 20%, #222 80%, transparent);
  }
  .contact {
    position: absolute;
    left: 420px;
    top: 70px;
    font-family: "Nunito Sans", sans-serif;
    color: var(--ink);
  }
  .person-name {
    margin: 0;
    font-size: 33px;
    font-weight: 800;
    line-height: 1;
  }
  .person-role {
    margin: 4px 0 34px;
    font-size: 17px;
    font-weight: 400;
  }
  .address {
    margin: 0 0 18px;
    font-size: 15px;
    line-height: 1.3;
    font-style: normal;
  }
  .lines {
    list-style: none;
    margin: 0;
    padding: 0;
    font-size: 16px;
    line-height: 1.4;
  }
  .lines li {
    display: flex;
    align-items: center;
    gap: 12px;
  }
  .lines svg {
    width: 13px;
    height: 13px;
    flex: none;
  }
  .footer-band {
    position: absolute;
    left: 0;
    right: 0;
    bottom: 0;
    height: 20px;
    background: var(--deep-blue);
  }
</style>
</head>
<body>
<div class="canvas">
  <section class="card card-back">
    <div class="back-brand">LodgeBridgely</div>
    <div class="back-url">LodgeBridgely.net</div>
  </section>

  <section class="card card-front">
    <div class="front-brand">LodgeBridgely</div>
    <div class="divider"></div>
    <div class="contact">
      <h1 class="person-name">Marcus Ellery</h1>
      <p class="person-role">Graphic Designer</p>
      <address class="address">
        2280 Alder Lane Suite 14<br>
        Fairbrook, IL 60999<br>
        Zip Code 604417
      </address>
      <ul class="lines">
        <li>
          <svg viewBox="0 0 12 12"><rect x="3" y="0.5" width="6" height="11" rx="1" fill="none" stroke="#1b1b1b" stroke-width="1.2"/><rect x="4.5" y="9" width="3" height="1" fill="#1b1b1b"/></svg>
          +1 555 0142 3380
        </li>
        <li>
          <svg viewBox="0 0 12 12"><path d="M2 1 L4.5 1 L5.5 3.5 L4 4.8 Q5.3 7.3 7.2 8 L8.5 6.5 L11 7.5 L11 10 Q6 11 2.5 6.5 Q1 4 2 1 Z" fill="#1b1b1b"/></svg>
          +1 555 0142 3381
        </li>
        <li>
          <svg viewBox="0 0 12 12"><rect x="0.5" y="2.5" width="11" height="7" fill="#1b1b1b"/><path d="M0.5 2.5 L6 7 L11.5 2.5" fill="none" stroke="#fff" stroke-width="1"/></svg>
          hello@lodgebridgely.net
        </li>
        <li>
          <svg viewBox="0 0 12 12"><circle cx="6" cy="6" r="5.2" fill="none" stroke="#1b1b1b" stroke-width="1"/><ellipse cx="6" cy="6" rx="2.3" ry="5.2" fill="none" stroke="#1b1b1b" stroke-width="0.8"/><line x1="0.8" y1="6" x2="11.2" y2="6" stroke="#1b1b1b" stroke-width="0.8"/></svg>
          lodgebridgely.net
        </li>
      </ul>
    </div>
    <div class="footer-band"></div>
  </section>
</div>
</body>
</html>
```